Velora, Pure Glow label sticker for cosmetic cream

I'm looking to design a label sticker for my cosmetic brand. The product is called Pure Glow. The brand is called Velora. I'm looking for a minimalistic, modern design that encapsulates the fact that the product is all natural. Made with 100% organic ingredients, vegan and cruelty free. The motto of the company is " The Healing Power of Nature"

Target Market(s)

Young professionals, 30+, 40+ interested in natural skin care

Industry/Entity Type

Cosmetic

Colors

Designer to choose only greyscale colors for use in the design.

Requirements
Must have
• Modern look, easily remembered but still a touch of nature

```html
<!DOCTYPE html>
<html lang="en">
<head>
<meta charset="utf-8">
<title>Velora Pure Glow — Label</title>
<link href="https://fonts.googleapis.com/css2?family=Montserrat:wght@400;500;600;700&display=swap" rel="stylesheet">
<style>
  :root {
    --page: #ffffff;
    --label: #0c0c0c;
    --ink: #d6d6d6;
    --ink-soft: #a8a8a8;
  }
  * { margin: 0; padding: 0; box-sizing: border-box; }
  html, body {
    width: 1200px;
    height: 1200px;
    overflow: hidden;
    background: var(--page);
  }
  .canvas {
    position: relative;
    width: 1200px;
    height: 1200px;
  }
  .label {
    position: absolute;
    left: 405px;
    top: 190px;
    width: 390px;
    height: 670px;
    background: var(--label);
    font-family: "Montserrat", sans-serif;
    color: var(--ink);
    text-align: center;
  }
  .brand-mark {
    position: absolute;
    left: 135px;
    top: 68px;
    width: 120px;
    height: 120px;
    border: 2px solid var(--ink);
    border-radius: 50%;
  }
  .brand-name {
    position: absolute;
    left: 0;
    right: 0;
    top: 206px;
    font-size: 40px;
    font-weight: 500;
    letter-spacing: 2px;
    line-height: 1;
  }
  .product-name {
    position: absolute;
    left: 0;
    right: 0;
    top: 318px;
    font-size: 48px;
    font-weight: 600;
    letter-spacing: 0.5px;
    line-height: 1;
    white-space: nowrap;
  }
  .tagline {
    position: absolute;
    left: 0;
    right: 0;
    top: 374px;
    font-size: 14.5px;
    font-weight: 400;
    letter-spacing: -0.2px;
    line-height: 1;
    white-space: nowrap;
    color: var(--ink-soft);
  }
  .badges {
    position: absolute;
    left: 0;
    right: 0;
    top: 490px;
    display: flex;
    justify-content: center;
    gap: 8px;
  }
  .badge {
    display: flex;
    flex-direction: column;
    align-items: center;
    width: 58px;
  }
  .badge-icon {
    width: 42px;
    height: 42px;
    display: block;
  }
  .badge-caption {
    margin-top: 8px;
    font-size: 7px;
    font-weight: 700;
    letter-spacing: 0.3px;
    white-space: nowrap;
    color: var(--ink);
  }
</style>
</head>
<body>
  <main class="canvas">
    <section class="label">
      <div class="brand-mark"></div>
      <div class="brand-name">VELORA</div>
      <h1 class="product-name">PURE GLOW</h1>
      <p class="tagline">THE HEALING POWER OF NATURE</p>
      <div class="badges">
        <div class="badge">
          <svg class="badge-icon" viewBox="0 0 42 42" aria-hidden="true">
            <circle cx="21" cy="21" r="20" fill="none" stroke="#d6d6d6" stroke-width="1.3"/>
            <path d="M13 29 C13 19 19 13 30 12 C30 23 24 29 13 29 Z" fill="none" stroke="#d6d6d6" stroke-width="1.4"/>
            <path d="M13 29 L25 17" stroke="#d6d6d6" stroke-width="1.2"/>
          </svg>
          <span class="badge-caption">ORGANIC</span>
        </div>
        <div class="badge">
          <svg class="badge-icon" viewBox="0 0 42 42" aria-hidden="true">
            <circle cx="21" cy="21" r="20" fill="none" stroke="#d6d6d6" stroke-width="1.3"/>
            <path d="M21 31 C13 26 13 16 21 10 C29 16 29 26 21 31 Z" fill="none" stroke="#d6d6d6" stroke-width="1.4"/>
            <path d="M21 31 L21 15" stroke="#d6d6d6" stroke-width="1.2"/>
          </svg>
          <span class="badge-caption">VEGAN</span>
        </div>
        <div class="badge">
          <svg class="badge-icon" viewBox="0 0 42 42" aria-hidden="true">
            <circle cx="21" cy="21" r="20" fill="none" stroke="#d6d6d6" stroke-width="1.3"/>
            <path d="M21 30 L13 22 C10 19 12 14 16 14 C18.5 14 20 15.5 21 17 C22 15.5 23.5 14 26 14 C30 14 32 19 29 22 Z" fill="none" stroke="#d6d6d6" stroke-width="1.4" stroke-linejoin="round"/>
          </svg>
          <span class="badge-caption">CRUELTY FREE</span>
        </div>
      </div>
    </section>
  </main>
</body>
</html>
```